Short Company Presentation (Indesign)

This is an easy project where most of the presentation document (provided in the attachment) is already designed. All that is needed is an exchange of text which I will provide as well as some small design management. Also some small new info graphics or illustrations may be nice to have if the designer is skilled to achieve this result. Any ideas from the designer are welcome and will be considered for future work.
Updates

Dear Designers, Please write me to find a time to integrate and begin collaborating on this presentation. Cheers, Brent Skype:Brentharlow

Reason: More time is needed to work on design briefs..

Reason: more time need to work on project

Target Market(s)

The target market is corporate executives

Industry/Entity Type

It Company

Requirements
Must have
• Ability to follow similar design pattern laid out in deck template

```html
<!DOCTYPE html>
<html lang="en">
<head>
<meta charset="utf-8">
<title>Veridane – Company Summary</title>
<link rel="stylesheet" href="https://fonts.googleapis.com/css2?family=Anton&family=PT+Sans:wght@400;700&family=Roboto+Condensed:wght@700;800&family=Open+Sans:wght@400&display=swap">
<style>
  :root {
    --ink: #111111;
    --paper: #ffffff;
    --rule: #555555;
    --brand-grey: #3c4350;
    --brand-accent: #f06a1c;
  }
  * { margin: 0; padding: 0; box-sizing: border-box; }
  html, body { width: 1200px; height: 900px; overflow: hidden; background: var(--paper); }
  .page { position: relative; width: 1200px; height: 900px; color: var(--ink); }

  .brand { position: absolute; left: 118px; top: 88px; display: flex; align-items: center; gap: 18px; }
  .brand-dot { width: 58px; height: 58px; border-radius: 50%; background: var(--brand-accent); }
  .brand-name { font-family: "Open Sans", sans-serif; font-weight: 400; font-size: 42px; color: var(--brand-grey); letter-spacing: -0.5px; }

  .disclaimer { position: absolute; left: 55px; top: 208px; width: 445px;
    font-family: "PT Sans", sans-serif; font-size: 14.3px; line-height: 19.2px; text-align: justify; }
  .disclaimer p { margin-bottom: 19px; }
  .disclaimer .legal { text-transform: uppercase; }

  .header-rule { position: absolute; left: 560px; width: 577px; height: 1.5px; background: var(--rule); }
  .header-rule.top { top: 51px; }
  .header-rule.bottom { top: 171px; }
  .section-title { position: absolute; right: 70px; top: 58px; text-align: right;
    font-family: "Anton", sans-serif; font-size: 57px; line-height: 52px; letter-spacing: 0.5px; }

  .metrics { position: absolute; left: 634px; top: 198px; width: 393px; height: 386px;
    border: 1.5px solid var(--rule); padding: 13px 14px 0; font-family: "Roboto Condensed", sans-serif; }
  .metrics-heading { background: var(--ink); color: var(--paper); height: 40px; padding-left: 15px;
    font-size: 21px; font-weight: 800; line-height: 40px; letter-spacing: 0.2px; margin-bottom: 22px; }
  .metrics-table { width: 100%; border-collapse: collapse; font-size: 12.5px; font-weight: 700; }
  .metrics-table td { border-bottom: 1.5px solid var(--ink); padding: 7px 0 4px 7px; vertical-align: bottom; height: 29.5px; }
  .metrics-table td.value { width: 142px; padding-left: 0; }
  .metrics-table tr.large td { font-size: 14px; }
  .metrics-table tr.first td { height: 38px; line-height: 14px; }
  .metrics-note { font-size: 11.3px; line-height: 13.5px; font-weight: 700; padding: 7px 4px 0 7px; }

  .notes { position: absolute; left: 640px; top: 594px; width: 380px; text-align: center;
    font-family: "Roboto Condensed", sans-serif; font-weight: 700; font-size: 11.2px; line-height: 13px; }
  .notes li { list-style: none; margin-bottom: 13px; }

  .section-badge { position: absolute; left: 1020px; top: 700px; width: 132px; height: 150px; }
</style>
</head>
<body>
<main class="page">
  <div class="brand">
    <span class="brand-dot"></span>
    <span class="brand-name">Veridane</span>
  </div>

  <section class="disclaimer">
    <p class="legal">This memorandum may not be read, circulated, distributed, reproduced, or otherwise used for any purpose other than the purpose described herein.</p>
    <p class="legal">We do not make any representations or warranties, express or implied, as to the accuracy or completeness of the information provided in this memorandum. We reserve the right to amend, replace and/or supplement this memorandum at any time and undertake no obligation to provide the recipient with access to additional information. Nothing in this memorandum is, or should be relied upon as, a promise or representation as to the future. The information contained in this memorandum does not purport to be all-inclusive or to contain all the information available.</p>
    <p class="legal">This memorandum does not constitute an offer to sell or a solicitation of an offer to buy securities. Such an offer or solicitation, if made, would be solely by way of the confidential private placement memorandum relating to the opportunities contemplated in this memorandum.</p>
    <p>This summary, which contains brief, selected information pertaining to the anticipated business and affairs of the company, has been prepared by Corvel Partners Ltd to provide general information about the company. This is not an offer to sell, or a solicitation of an offer to buy securities, as such an offer or solicitation can only come through the offering’s PPM. This material cannot, and does not, replace the PPM, and the PPM supersedes this material in all respects. This investment involves various degrees of risk, including the speculative market and financing risks associated with fluctuations in the real estate market including tax status, liquidity, and fees, expenses, and other risk factors. Please refer to the “Risk Factors” section of the PPM.</p>
  </section>

  <div class="header-rule top"></div>
  <h1 class="section-title">COMPANY<br>SUMMARY</h1>
  <div class="header-rule bottom"></div>

  <section class="metrics">
    <h2 class="metrics-heading">KEY INVESTMENT METRICS</h2>
    <table class="metrics-table">
      <tr class="first"><td>PROJECTED<br>YIELD OVER THE HOLD</td><td class="value">9.6%</td></tr>
      <tr class="large"><td>FUND SIZE</td><td class="value">$ 300M - 1,000M</td></tr>
      <tr><td>MINIMUM INV. SIZE</td><td class="value">$ 10M</td></tr>
      <tr><td>MANAGEMENT FEES</td><td class="value">1%annual</td></tr>
      <tr><td>ASSET CLASS</td><td class="value">GROUND LEASE</td></tr>
      <tr><td>TARGET INVESTMENT SIZE</td><td class="value">$3M - 20M</td></tr>
      <tr><td>PREFERRED RETURN</td><td class="value">8%</td></tr>
      <tr><td>TERM</td><td class="value">5 YEARS</td></tr>
    </table>
    <p class="metrics-note">First close of the Fund is projected in 2011Q2. The projected yield over the hold period is based on specific assumptions in the Private Placement Memorandom of the Fund (the “PPM”) including the project exit scenarios.</p>
  </section>

  <ul class="notes">
    <li>• The Manager, Veridane, will manage the Fund portfolio on behalf of investors during the hold period.</li>
    <li>• Distributions from available cash flow will be made quarterly to the investors pursuant to terms of the PPM and the Limited Liability Company Agreement (the “LLC Agreement”) of the Fund.</li>
  </ul>

  <svg class="section-badge" viewBox="0 0 132 150" aria-label="Summary section 1">
    <defs>
      <path id="badge-arc" d="M 14 60 A 52 52 0 0 1 118 60"/>
    </defs>
    <text font-family="Roboto Condensed, sans-serif" font-weight="800" font-size="17" letter-spacing="1.5" fill="#111111">
      <textPath href="#badge-arc" startOffset="50%" text-anchor="middle">SUMMARY</textPath>
    </text>
    <circle cx="65" cy="78" r="57" fill="#111111"/>
    <text x="66" y="120" text-anchor="middle" font-family="Anton, sans-serif" font-size="92" fill="#ffffff">1</text>
  </svg>
</main>
</body>
</html>
```